Harrowgate Distillery Bottle Label Design

We need a label design for a product called "Cedar Lorne Straight Bourbon Whiskey". The bottle has two embossments on the side and an image printed on the back that will show through when looking from the front (shown in the attached image). It's made of 30% rye and 70% corn; images of the ingredients can be incorporated into the label design. We are a distillery that produces whiskey and bourbon from local farmers around the area. We focus on the quality of the ingredients and using the recipes passed down from generation to generation. We like a straight forward design using two colors maximum. The background will be brown once filled with the bourbon, so it must contrast against it (i.e. white and other lighter colors). The Harrowgate Distillery logo must be present on the bottle front, as well as 750 ml, 84 PROOF, 42% ALC/VOL.

Target Market(s)

Craft whiskey consumers.

Industry/Entity Type

Product

Colors
fee18a
fbe7d2
fff3d1
fefcee
fefdec
fdf9cf

Requirements
Must have
• 750 ml, 84 PROOF, 42% ALC/VOL. Aged for 3 years.The Harrowgate Distillery logo must be present on the bottle. Only two colors on label.
Nice to have
• Story of how we are a micro distillery making hand crafted whiskey.
Should not have
• False or misleading print.

```html
<!DOCTYPE html>
<html lang="en">
<head>
<meta charset="utf-8">
<title>Harrowgate Distillery – Cedar Lorne Straight Bourbon Whiskey Label</title>
<link rel="stylesheet" href="https://fonts.googleapis.com/css2?family=Stint+Ultra+Condensed&family=Ultra&family=Vollkorn:wght@400;700&display=swap">
<style>
  :root {
    --label-stock: #ffffff;
    --bourbon-brown: #3e2224;
    --grain-yellow: #fff200;
  }
  * { margin: 0; padding: 0; box-sizing: border-box; }
  html, body { width: 1200px; height: 999px; overflow: hidden; background: var(--label-stock); }
  .label {
    position: relative; width: 1200px; height: 999px; display: flex;
    font-variant-numeric: lining-nums;
  }

  .front {
    width: 600px; height: 999px; background: var(--label-stock);
    color: var(--bourbon-brown); text-align: center; position: relative;
  }
  .brand {
    position: absolute; top: 88px; left: 0; width: 600px;
    display: flex; flex-direction: column; align-items: center;
  }
  .brand-dot { width: 58px; height: 58px; border-radius: 50%; background: var(--bourbon-brown); margin-bottom: 16px; }
  .brand-name {
    font-family: "Vollkorn", serif; font-weight: 700; font-size: 30px;
    line-height: 1.05; color: var(--bourbon-brown);
  }
  .product-name {
    position: absolute; top: 272px; left: 0; width: 600px;
    font-family: "Stint Ultra Condensed", serif; font-weight: 400; font-size: 64px; line-height: 1;
    letter-spacing: 3px;
  }
  .product-type {
    position: absolute; top: 340px; left: 0; width: 600px;
    font-family: "Ultra", "Rockwell", serif; font-weight: 400; font-size: 62px; line-height: 71px;
  }
  .age {
    position: absolute; top: 572px; left: 0; width: 600px;
    font-family: "Stint Ultra Condensed", serif; font-size: 34px; letter-spacing: 2px;
  }
  .proof {
    position: absolute; top: 690px; left: 0; width: 600px;
    font-family: "Vollkorn", serif; font-weight: 700; font-size: 30px;
  }
  .drop { position: absolute; top: 783px; left: 267px; width: 68px; height: 111px; }

  .back {
    width: 600px; height: 999px; background: var(--bourbon-brown);
    color: var(--label-stock); position: relative; text-align: center;
  }
  .story {
    position: absolute; top: 164px; left: 0; width: 600px;
    font-family: "Vollkorn", serif; font-size: 33px; line-height: 45.3px;
  }
  .story .initial { font-size: 52px; line-height: 0; }
  .grain-bill {
    position: absolute; top: 781px; left: 0; width: 600px; height: 53px; display: flex;
    font-family: "Vollkorn", serif; font-weight: 700; font-size: 29px;
    border-top: 2px solid var(--grain-yellow); border-bottom: 2px solid var(--grain-yellow);
  }
  .grain-rye {
    width: 179px; background: var(--bourbon-brown); color: var(--grain-yellow);
    display: flex; align-items: center; justify-content: center;
  }
  .grain-corn {
    flex: 1; background: var(--grain-yellow); color: var(--bourbon-brown);
    display: flex; align-items: center; justify-content: center;
  }
  .volume {
    position: absolute; top: 864px; left: 0; width: 600px;
    font-family: "Vollkorn", serif; font-weight: 700; font-size: 30px; line-height: 38px;
  }
</style>
</head>
<body>
<main class="label">
  <section class="front">
    <div class="brand">
      <span class="brand-dot"></span>
      <span class="brand-name">Harrowgate Distillery</span>
    </div>
    <h1 class="product-name">Cedar Lorne</h1>
    <h2 class="product-type">STRAIGHT<br>BOURBON<br>WHISKEY.</h2>
    <p class="age">Aged 3 Years</p>
    <p class="proof">84 Proof</p>
    <svg class="drop" viewBox="0 0 68 111" aria-hidden="true">
      <path d="M34 0 C40 28 68 56 68 77 A34 34 0 0 1 0 77 C0 56 28 28 34 0 Z" fill="var(--bourbon-brown)"/>
    </svg>
  </section>

  <section class="back">
    <p class="story"><span class="initial">T</span>here’s nothing complicated<br>
      about Cedar Lorne Straight<br>
      Bourbon. Local farmers supply<br>
      home-grown ingredients, and we<br>
      supply our family recipe. Once<br>
      distilled, it rests three years in<br>
      oak, then our bourbon is bottled<br>
      and shipped to the masses.<br>
      Quality and consistency are our<br>
      trademark, using tried and true<br>
      methods passed down from<br>
      generation to generation… and<br>
      into your glass. Enjoy.</p>
    <div class="grain-bill">
      <span class="grain-rye">30% Rye</span>
      <span class="grain-corn">70% corn</span>
    </div>
    <p class="volume">42% alcohol<br>750 ml.</p>
  </section>
</main>
</body>
</html>
```